Business Card Update, need to bring life to the card, two sided color

We need a new business card design, are moving and changing addresses and need a new look, we have the logos already attached but need a new style moving forward. Can incorporate the color of the logo (The Green) as well, maybe a solid back? We deal with safety products revolving around static electricity and safety lighting. Would like to keep same font in second logo as well.

Target Market(s)

Electrical Safety, Lighting

Contact Information for Business Card

Lars Whitcombe
Vice President
Office: 555-284-7316
Cell: 555-862-0457
lars@tkwhitcombe.com
www.tkwhitcombe.com
4700 West Cedar Boulevard
Suite #320
Roswell, GA 30412

Font styles to use
Serif
Sans Serif

Requirements
Must have
• Since 1918
Nice to have
• Could use the 100 Year Logo for back of card, would like the back of card to be the same green as logo.
Should not have
• No black cards please.

```html
<!DOCTYPE html>
<html lang="en">
<head>
<meta charset="utf-8">
<title>T.K. Whitcombe – Business Card</title>
<link href="https://fonts.googleapis.com/css2?family=Roboto+Condensed:wght@400;700&display=swap" rel="stylesheet">
<style>
  :root {
    --brand-green: #0fa052;
    --brand-green-dark: #0b8a45;
    --card-white: #f4f4f2;
    --stage: #2e2f31;
    --ink-light: #ffffff;
  }
  * { box-sizing: border-box; margin: 0; padding: 0; }
  html, body {
    width: 1200px; height: 900px; overflow: hidden;
    background: var(--stage);
    font-family: "Roboto Condensed", "Arial Narrow", sans-serif;
  }
  .canvas {
    width: 1200px; height: 900px;
    display: flex; flex-direction: column; align-items: center; justify-content: center;
    gap: 60px;
  }
  .card {
    width: 560px; height: 320px; position: relative; overflow: hidden;
    box-shadow: 0 10px 30px rgba(0,0,0,.45);
  }

  /* Back */
  .card-back {
    background: var(--brand-green);
    display: flex; flex-direction: column; align-items: center; justify-content: center; gap: 14px;
  }
  .back-brand { display: flex; align-items: center; gap: 18px; }
  .back-mark {
    width: 58px; height: 58px; border-radius: 50%;
    background: var(--ink-light); opacity: .9;
  }
  .back-name {
    color: var(--ink-light); font-weight: 700; font-size: 46px;
    letter-spacing: 1px; text-transform: uppercase;
  }
  .back-since {
    background: rgba(255,255,255,.22);
    color: var(--ink-light); font-weight: 700; font-size: 22px;
    letter-spacing: 3px; text-transform: uppercase;
    padding: 4px 18px;
  }

  /* Front */
  .card-front { background: var(--card-white); }
  .front-logo {
    position: absolute; left: 0; right: 0; top: 56px;
    display: flex; align-items: center; justify-content: center; gap: 12px;
  }
  .front-logo-mark {
    width: 44px; height: 44px; border-radius: 50%; background: var(--brand-green);
  }
  .front-logo-name {
    color: var(--brand-green); font-weight: 700; font-size: 30px;
    text-transform: uppercase; letter-spacing: .5px;
  }
  .front-rule {
    position: absolute; left: 30px; right: 30px; top: 182px; height: 2px;
    background: var(--brand-green);
  }
  .identity {
    position: absolute; left: 30px; top: 200px; width: 240px;
  }
  .identity-name {
    color: var(--brand-green-dark); font-weight: 700; font-size: 28px; line-height: 1.1;
  }
  .identity-title {
    color: var(--brand-green); font-size: 17px; margin-top: 4px;
  }
  .contact-list {
    position: absolute; right: 30px; top: 194px; list-style: none;
  }
  .contact-list li {
    display: flex; align-items: center; gap: 8px;
    color: var(--brand-green); font-size: 14px; line-height: 19px;
  }
  .contact-label { font-weight: 700; width: 38px; }
  .contact-list svg { width: 13px; height: 13px; fill: var(--brand-green); flex: none; }
  .address-band {
    position: absolute; left: 0; right: 0; bottom: 0; height: 36px;
    background: var(--brand-green);
    color: var(--ink-light); font-size: 14px; letter-spacing: .3px;
    display: flex; align-items: center; justify-content: flex-end; padding-right: 30px;
  }
</style>
</head>
<body>
<main class="canvas">

  <section class="card card-back" aria-label="Card back">
    <div class="back-brand">
      <span class="back-mark"></span>
      <span class="back-name">T.K. Whitcombe</span>
    </div>
    <span class="back-since">Since 1918</span>
  </section>

  <section class="card card-front" aria-label="Card front">
    <div class="front-logo">
      <span class="front-logo-mark"></span>
      <span class="front-logo-name">T.K. Whitcombe</span>
    </div>

    <div class="front-rule"></div>

    <div class="identity">
      <p class="identity-name">Lars Whitcombe</p>
      <p class="identity-title">Vice President</p>
    </div>

    <ul class="contact-list">
      <li>
        <svg viewBox="0 0 24 24" aria-hidden="true"><path d="M6.6 10.8a15.1 15.1 0 0 0 6.6 6.6l2.2-2.2c.3-.3.7-.4 1-.2 1.1.4 2.3.6 3.6.6.6 0 1 .4 1 1V20c0 .6-.4 1-1 1A17 17 0 0 1 3 4c0-.6.4-1 1-1h3.5c.6 0 1 .4 1 1 0 1.3.2 2.5.6 3.6.1.3 0 .7-.2 1z"/></svg>
        <span class="contact-label">Office</span> 555-284-7316
      </li>
      <li>
        <svg viewBox="0 0 24 24" aria-hidden="true"><path d="M7 2h10a2 2 0 0 1 2 2v16a2 2 0 0 1-2 2H7a2 2 0 0 1-2-2V4a2 2 0 0 1 2-2zm0 3v13h10V5zm5 14.2a1 1 0 1 0 0 .1z"/></svg>
        <span class="contact-label">Cell</span> 555-862-0457
      </li>
      <li>
        <svg viewBox="0 0 24 24" aria-hidden="true"><path d="M2 5h20v14H2zm2 2v.5l8 5 8-5V7zm0 2.9V17h16V9.9l-8 5z"/></svg>
        lars@tkwhitcombe.com
      </li>
      <li>
        <svg viewBox="0 0 24 24" aria-hidden="true"><path d="M12 2a10 10 0 1 0 0 20 10 10 0 0 0 0-20zm6.9 6h-3a15 15 0 0 0-1.3-3.9A8 8 0 0 1 18.9 8zM12 4c.8 1.2 1.5 2.5 1.9 4h-3.8c.4-1.5 1.1-2.8 1.9-4zM4.3 14a8 8 0 0 1 0-4h3.4a16 16 0 0 0 0 4zm.8 2h3a15 15 0 0 0 1.3 3.9A8 8 0 0 1 5.1 16zm3-8h-3a8 8 0 0 1 4.3-3.9C8.8 5.3 8.4 6.6 8.1 8zM12 20c-.8-1.2-1.5-2.5-1.9-4h3.8c-.4 1.5-1.1 2.8-1.9 4zm2.3-6H9.7a14 14 0 0 1 0-4h4.6a14 14 0 0 1 0 4zm.3 5.9c.6-1.2 1-2.5 1.3-3.9h3a8 8 0 0 1-4.3 3.9zM16.3 14a16 16 0 0 0 0-4h3.4a8 8 0 0 1 0 4z"/></svg>
        www.tkwhitcombe.com
      </li>
    </ul>

    <div class="address-band">4700 West Cedar Boulevard, Suite #320, Roswell, GA 30412</div>
  </section>

</main>
</body>
</html>
```